Sign Advertisment for Condominium Development

I need a sign created that will be placed in front of a building that is being converted into a luxury condominium development.

The sign needs to say:

Two, Boutique Luxury Condominiums Delivering late 2015.

Luxury Finishes // Designer Kitchens and Bath // Each Unit over 2,000 Square Feet

Deeded Parking Included with Each Unit

To Learn More, Contact:

Loretta Pinwell or Morgan Tesh
(202) 555-0147
Loretta.Pinwell@nrg-example.com

I need a small disclaimer at the bottom stating:

These Condominium(s) have not been registered by the Office of Residential Property Oversight Bureau of Dwelling Registration Tenancy Transfer and Purchase Section. A Condominium Unit may be reserved on a non-binding reservation agreement, but no contract of sale or lease that is binding on the purchaser may be entered into prior to registration.

Target Market(s)

Young professionals seeking luxury condominium

Industry/Entity Type

Building

Font styles to use
Serif

Colors
00a88f
ffffff

```html
<!DOCTYPE html>
<html lang="en">
<head>
<meta charset="utf-8">
<title>Boutique Luxury Condominiums Sign</title>
<link rel="stylesheet" href="https://fonts.googleapis.com/css2?family=Arvo:wght@700&family=Hind:wght@300;400;600&display=swap">
<style>
  :root {
    --sign-green: #00a88f;
    --ink-white: #ffffff;
    --backdrop: #f2f1ec;
  }
  * { box-sizing: border-box; margin: 0; padding: 0; }
  html, body {
    width: 1200px;
    height: 1000px;
    overflow: hidden;
    background: var(--backdrop);
  }
  .canvas {
    position: relative;
    width: 1200px;
    height: 1000px;
  }
  .sign {
    position: absolute;
    left: 40px;
    top: 135px;
    width: 1120px;
    height: 730px;
    background: var(--sign-green);
    color: var(--ink-white);
    font-family: "Hind", sans-serif;
  }
  .headline {
    position: absolute;
    left: 0;
    top: 52px;
    width: 100%;
    text-align: center;
    font-family: "Arvo", serif;
    font-weight: 700;
    font-size: 50px;
    line-height: 64px;
  }
  .headline .unit-count {
    font-size: 68px;
  }
  .features {
    position: absolute;
    left: 99px;
    top: 245px;
    list-style: none;
    font-size: 29px;
    font-weight: 600;
    line-height: 37.5px;
  }
  .features .light { font-weight: 400; }
  .contact {
    position: absolute;
    left: 107px;
    top: 455px;
    font-size: 26px;
    line-height: 39px;
  }
  .contact-intro {
    font-weight: 300;
    padding-left: 42px;
  }
  .contact-row {
    display: flex;
    align-items: center;
    gap: 16px;
    font-weight: 600;
  }
  .contact-row .conj { font-weight: 400; }
  .contact-row .plain { font-weight: 400; }
  .contact-icon {
    width: 30px;
    height: 26px;
    flex: none;
  }
  .partners {
    position: absolute;
    left: 790px;
    top: 420px;
    width: 240px;
    display: flex;
    flex-direction: column;
    align-items: center;
    gap: 34px;
  }
  .partner {
    display: flex;
    align-items: center;
    gap: 10px;
    font-size: 22px;
    font-weight: 600;
    letter-spacing: 0.5px;
    white-space: nowrap;
  }
  .partner-mark {
    width: 14px;
    height: 14px;
    background: var(--ink-white);
  }
  .partner-mark.round { border-radius: 50%; }
  .disclaimer {
    position: absolute;
    left: 30px;
    right: 30px;
    top: 650px;
    text-align: center;
    font-size: 17.5px;
    font-weight: 300;
    line-height: 22px;
  }
</style>
</head>
<body>
<main class="canvas">
  <section class="sign">
    <h1 class="headline">
      <span class="unit-count">2</span> Boutique Luxury Condominiums<br>
      Delivering late 2015.
    </h1>

    <ul class="features">
      <li>Luxury Finishes</li>
      <li>Designer Kitchens and Bath</li>
      <li>Each Unit over <span class="light">2,000 Square Feet</span></li>
      <li>Deeded Parking Included with Each Unit</li>
    </ul>

    <div class="contact">
      <p class="contact-intro">To Learn More, Contact:</p>
      <p class="contact-row">
        <svg class="contact-icon" viewBox="0 0 30 26" aria-hidden="true">
          <circle cx="15" cy="7" r="6" fill="#fff"/>
          <path d="M3 25 C3 16 27 16 27 25 Z" fill="#fff"/>
        </svg>
        <span>Loretta Pinwell <span class="conj">or</span> Morgan Tesh</span>
      </p>
      <p class="contact-row">
        <svg class="contact-icon" viewBox="0 0 30 26" aria-hidden="true">
          <path d="M8 2 L12 7 L9.5 10 C11 14 14 17 18 18.5 L21 16 L26 20 L23 24 C14 24 5 14 5 5 Z" fill="none" stroke="#fff" stroke-width="2" stroke-linejoin="round"/>
        </svg>
        <span class="plain">(202) 555-0147</span>
      </p>
      <p class="contact-row">
        <svg class="contact-icon" viewBox="0 0 30 26" aria-hidden="true">
          <rect x="2" y="5" width="26" height="17" fill="#fff"/>
          <path d="M2 5 L15 15 L28 5" fill="none" stroke="#00a88f" stroke-width="2"/>
        </svg>
        <span class="plain">Loretta.Pinwell@nrg-example.com</span>
      </p>
    </div>

    <div class="partners">
      <p class="partner"><span class="partner-mark"></span>HARWELL FINE PROPERTIES</p>
      <p class="partner">NORROW CONSTRUCTION</p>
      <p class="partner"><span class="partner-mark round"></span>RIDGEWAY BANK</p>
    </div>

    <p class="disclaimer">
      These Condominium(s) have not been registered by the Office of Residential Property Oversight Bureau of Dwelling Registration Tenancy Transfer and Purchase Section. A Condominium Unit may be reserved on a non-binding reservation agreement, but no contract of sale or lease that is binding on the purchaser may be entered into prior to registration.
    </p>
  </section>
</main>
</body>
</html>
```